Roofing company needs a door hanger designed.

Hello, I would like to have a door hanger designed for our roofing company in Orlando Florida. I have included information about us below and attached our logo. Please let me know if there is anything else you need? thank you.

BRIGHT HARBOR ROOFING
5417 Copper Meadow Blvd. Winter Park, FL 32795
Website: brightharborroofco.example
Email: info@brightharborroofco.example
Office phone #: 407.555.0146

Notes: In the state of Florida a roofing contractor must include their license number on all documentation and marketing materials. Lic#CCC1590827

Items I would like to add:
-CALL TODAY FOR A FREE ESTIMATE
-SCHEDULE YOUR FREE INSPECTION TODAY
-OUR SERVICES: ROOF REPLACEMENT, ROOF REPAIR, EMERGENCY SERVICES
-LICENSED & INSURED
OTHER SENTENCES / PARAGRAPHS IF NEEDED.
-We at Bright Harbor Roofing are dedicated to providing superior service.
-Driven to offer the highest quality and professional commercial and residential roofing solutions at a fair price.
-Our goal is to provide you with the best value possible!
-The best option not the highest priced option. Sometimes a small roof repair is all it takes to fix your roofing issues.
-Free roof inspections and proposals that are customized to your project to solve your roofing needs.

```html
<!DOCTYPE html>
<html lang="en">
<head>
<meta charset="utf-8">
<title>Bright Harbor Roofing – Door Hanger</title>
<link rel="stylesheet" href="https://fonts.googleapis.com/css2?family=Roboto+Mono:wght@400;700&family=Poppins:wght@800&display=swap">
<style>
  :root {
    --backdrop: #ece8df;
    --hanger-yellow: #fac523;
    --brand-blue: #2c62b5;
    --sun-orange: #f6a21c;
    --ink: #141414;
    --hole: #3a3220;
    --white: #ffffff;
  }
  html, body {
    margin: 0;
    padding: 0;
    width: 892px;
    height: 1200px;
    overflow: hidden;
    background: var(--backdrop);
  }
  .door-hanger {
    display: block;
    width: 892px;
    height: 1200px;
  }
  .hanger-face { fill: var(--hanger-yellow); }
  .hang-hole { fill: var(--hole); }
  .license {
    font-family: "Roboto Mono", monospace;
    font-size: 10px;
    fill: var(--ink);
  }
  .brand-mark { fill: var(--sun-orange); }
  .brand-name {
    font-family: "Roboto Mono", monospace;
    font-weight: 700;
    font-size: 44px;
    fill: var(--brand-blue);
  }
  .service {
    font-family: "Roboto Mono", monospace;
    font-weight: 700;
    font-size: 56px;
    fill: var(--brand-blue);
  }
  .phone-bar { fill: var(--brand-blue); }
  .phone-icon { fill: var(--white); }
  .phone-number {
    font-family: "Poppins", sans-serif;
    font-weight: 800;
    font-size: 60px;
    fill: var(--white);
  }
  .call-to-action {
    font-family: "Roboto Mono", monospace;
    font-weight: 700;
    font-size: 26px;
    fill: var(--brand-blue);
  }
  .rim-text {
    font-family: "Roboto Mono", monospace;
    fill: var(--ink);
  }
  .rim-side { font-size: 21px; }
  .rim-website { font-size: 26px; }
</style>
</head>
<body>
<svg class="door-hanger" width="892" height="1200" viewBox="0 0 892 1200" xmlns="http://www.w3.org/2000/svg">
  <defs>
    <path id="rim-clockwise" d="M446 975 A375 375 0 1 1 446 225 A375 375 0 1 1 446 975"/>
    <path id="rim-bottom" d="M54 600 A392 392 0 0 0 838 600"/>
  </defs>

  <circle class="hanger-face" cx="446" cy="600" r="420"/>
  <circle class="hang-hole" cx="273" cy="261" r="7"/>
  <circle class="hang-hole" cx="636" cy="264" r="7"/>

  <text class="license" x="446" y="214" text-anchor="middle">LIC#CCC1590827</text>

  <g class="brand">
    <circle class="brand-mark" cx="336" cy="305" r="36"/>
    <text class="brand-name" x="446" y="395" text-anchor="middle">BRIGHT HARBOR</text>
    <text class="brand-name" x="446" y="445" text-anchor="middle">ROOFING</text>
  </g>

  <g class="services">
    <text class="service" x="446" y="548" text-anchor="middle">ROOF REPLACEMENT</text>
    <text class="service" x="446" y="603" text-anchor="middle">ROOF REPAIR</text>
    <text class="service" x="446" y="658" text-anchor="middle">EMERGENCY SERVICES</text>
  </g>

  <g class="phone">
    <rect class="phone-bar" x="187" y="738" width="517" height="60"/>
    <path class="phone-icon" transform="translate(196 745) scale(1.9)" d="M6.62 10.79c1.44 2.83 3.76 5.14 6.59 6.59l2.2-2.2c.27-.27.67-.36 1.02-.24 1.12.37 2.33.57 3.57.57.55 0 1 .45 1 1V20c0 .55-.45 1-1 1-9.39 0-17-7.61-17-17 0-.55.45-1 1-1h3.5c.55 0 1 .45 1 1 0 1.25.2 2.45.57 3.57.11.35.03.74-.25 1.02l-2.2 2.2z"/>
    <text class="phone-number" x="474" y="791" text-anchor="middle">407.555.0146</text>
  </g>
  <text class="call-to-action" x="446" y="827" text-anchor="middle">CALL TODAY FOR A FREE ESTIMATE</text>

  <text class="rim-text rim-side">
    <textPath href="#rim-clockwise" startOffset="27.2%" text-anchor="middle">Email: info@brightharborroofco.example</textPath>
  </text>
  <text class="rim-text rim-side">
    <textPath href="#rim-clockwise" startOffset="71.4%" text-anchor="middle">5417 Copper Meadow Blvd. Winter Park, FL 32795</textPath>
  </text>
  <text class="rim-text rim-website">
    <textPath href="#rim-bottom" startOffset="50%" text-anchor="middle">www.brightharborroofco.example</textPath>
  </text>
</svg>
</body>
</html>
```